New Business Card Design Project

The legal name of the company is TTTolvane, we also refer to it as simply Tolvane or you could also use the initials TTT...... please feel creative.
Excellent design.
On the second side, if you could image North and South America on each drop of water ... it almost looks like that now.
The website is www.tttolvane.com
Attached is another card with the required information; no addresses.

Industry/Entity Type

Legal

```html
<!DOCTYPE html>
<html lang="en">
<head>
<meta charset="utf-8">
<title>TTTolvane Business Card</title>
<link href="https://fonts.googleapis.com/css2?family=Encode+Sans+Condensed:wght@200;400&family=Open+Sans:wght@400;700&display=swap" rel="stylesheet">
<style>
  :root {
    --page: #e9e9ea;
    --blue-light: #1fb4ec;
    --blue-mid: #1683d3;
    --blue-deep: #2a3fae;
    --blue-accent: #1e9be0;
    --card-dark: #0f181b;
    --card-dark-2: #152125;
    --text-light: #f2f6f8;
    --text-muted: #9aa4a8;
  }
  * { margin: 0; padding: 0; box-sizing: border-box; }
  html, body { width: 1200px; height: 800px; overflow: hidden; background: var(--page); }
  .canvas { position: relative; width: 1200px; height: 800px; }

  /* Front side */
  .card-front {
    position: absolute; left: 110px; top: 110px; width: 330px; height: 580px;
    overflow: hidden;
    background: linear-gradient(180deg, var(--blue-light) 0%, var(--blue-mid) 45%, var(--blue-deep) 100%);
    box-shadow: 0 10px 30px rgba(0,0,0,.25);
  }
  .card-front .top-curve { position: absolute; left: 0; top: 0; width: 330px; height: 230px; }
  .front-wordmark {
    position: absolute; left: 170px; top: 255px;
    writing-mode: vertical-rl;
    font-family: "Encode Sans Condensed", sans-serif; font-weight: 200;
    font-size: 78px; letter-spacing: 2px; color: var(--text-light); line-height: 1;
  }
  .front-url {
    position: absolute; left: 138px; top: 262px;
    writing-mode: vertical-rl;
    font-family: "Open Sans", sans-serif; font-size: 17px; letter-spacing: 4.5px;
    color: var(--text-light);
  }

  /* Back side */
  .card-back {
    position: absolute; left: 490px; top: 215px; width: 620px; height: 370px;
    overflow: hidden;
    background: linear-gradient(160deg, var(--card-dark) 0%, var(--card-dark-2) 100%);
    box-shadow: 0 10px 30px rgba(0,0,0,.3);
    font-family: "Open Sans", sans-serif;
  }
  .card-back .frame-lines { position: absolute; inset: 0; }
  .globe {
    position: absolute; left: 250px; top: 110px; width: 460px; height: 460px; border-radius: 50%;
    background: radial-gradient(circle at 45% 35%, #3fc0f2 0%, #1a86d4 45%, #1a4fb0 100%);
    border: 8px solid #1b6fb8;
  }
  .person { position: absolute; left: 230px; top: 30px; }
  .person-name { font-weight: 700; font-size: 22px; color: var(--blue-accent); letter-spacing: 1px; }
  .person-title { font-size: 13px; color: var(--text-muted); margin-top: 2px; }
  .contact-list { position: absolute; left: 185px; top: 104px; list-style: none; }
  .contact-list li {
    display: flex; align-items: center; gap: 8px;
    font-size: 13px; color: var(--text-light); line-height: 20px;
  }
  .contact-list .icon { width: 13px; height: 13px; }
  .back-url { position: absolute; left: 30px; top: 200px; font-size: 13px; color: var(--blue-accent); }
  .back-logo { position: absolute; left: 290px; top: 182px; display: flex; align-items: center; gap: 14px; }
  .back-logo .mark { width: 56px; height: 56px; border-radius: 50%; background: var(--text-light); }
  .back-logo .name {
    font-family: "Encode Sans Condensed", sans-serif; font-weight: 200;
    font-size: 54px; letter-spacing: 1px; color: var(--text-light); line-height: 1;
  }
</style>
</head>
<body>
<main class="canvas">

  <section class="card-front">
    <svg class="top-curve" viewBox="0 0 330 230" aria-hidden="true">
      <path d="M0 0 H330 V120 Q250 225 95 222 Q40 220 0 200 Z" fill="#1c6fc9" opacity=".55"/>
    </svg>
    <div class="front-wordmark">TOLVANE</div>
    <div class="front-url">www.tttolvane.com</div>
  </section>

  <section class="card-back">
    <div class="globe" role="img" aria-label="Globe showing North and South America"></div>

    <svg class="frame-lines" viewBox="0 0 620 370" aria-hidden="true">
      <path d="M225 88 H400 V150" fill="none" stroke="#1e9be0" stroke-width="1.2"/>
      <path d="M20 184 H235 V268" fill="none" stroke="#1e9be0" stroke-width="1.2"/>
      <rect x="231" y="266" width="8" height="8" fill="#1e9be0"/>
    </svg>

    <div class="person">
      <div class="person-name">LEO BRANDT</div>
      <div class="person-title">Managing Director</div>
    </div>

    <ul class="contact-list">
      <li><svg class="icon" viewBox="0 0 14 14" aria-hidden="true"><circle cx="7" cy="7" r="7" fill="#1e9be0"/><path d="M4.5 3.5 L6 5 L5.2 6.2 Q6.2 8 7.8 8.8 L9 8 L10.5 9.5 L9.5 10.5 Q6 10 3.5 4.5 Z" fill="#0f181b"/></svg>USA: +1 (555) 014 2270</li>
      <li><svg class="icon" viewBox="0 0 14 14" aria-hidden="true"><circle cx="7" cy="7" r="7" fill="#1e9be0"/><path d="M4.5 3.5 L6 5 L5.2 6.2 Q6.2 8 7.8 8.8 L9 8 L10.5 9.5 L9.5 10.5 Q6 10 3.5 4.5 Z" fill="#0f181b"/></svg>Guatemala: +502 5550 0187</li>
      <li><svg class="icon" viewBox="0 0 14 14" aria-hidden="true"><circle cx="7" cy="7" r="7" fill="#1e9be0"/><rect x="3.5" y="4.5" width="7" height="5" fill="none" stroke="#0f181b" stroke-width="1"/><path d="M3.5 4.5 L7 7.5 L10.5 4.5" fill="none" stroke="#0f181b" stroke-width="1"/></svg>lb@tttolvane.com</li>
    </ul>

    <div class="back-url">www.tttolvane.com</div>

    <div class="back-logo">
      <span class="mark"></span>
      <span class="name">TOLVANE</span>
    </div>
  </section>

</main>
</body>
</html>
```